High end Electrical/home automation Business Card

Need a card for a high end electrical and home automation company utilising the existing logo.
Phone
Email
Website

Like black look with raised detail. Don’t necessarily need to keep colour of logo it could be made grayscale or white etc

Target Market(s)

High end clients

Contact Information for Business Card

Ridgeline Electrical

Requirements
Must have
• Logo, phone, email, website, address

High end look
Nice to have
• Black background card
Raised font
Should not have
• Lots of colour

```html
<!DOCTYPE html>
<html lang="en">
<head>
<meta charset="UTF-8">
<title>Ridgeline Electrical — Business Card</title>
<link rel="stylesheet" href="https://fonts.googleapis.com/css2?family=Archivo:wght@700&family=Work+Sans:wght@400;500&display=swap">
<style>
  :root {
    --stage: #1e1e1f;
    --card: #1a1a1b;
    --card-edge: #232324;
    --pattern-a: #2a2a2b;
    --pattern-b: #141415;
    --white: #f4f4f4;
    --blue: #1a8fd6;
  }
  * { margin: 0; padding: 0; box-sizing: border-box; }
  html, body { width: 1200px; height: 900px; overflow: hidden; }
  body {
    background: var(--stage);
    display: flex;
    flex-direction: column;
    align-items: center;
    justify-content: center;
    gap: 40px;
    font-family: "Work Sans", sans-serif;
  }
  .card {
    position: relative;
    width: 680px;
    height: 388px;
    background: var(--card);
    border: 1px solid var(--card-edge);
    overflow: hidden;
  }
  /* Front */
  .card-front__pattern {
    position: absolute;
    inset: 0;
    background: radial-gradient(ellipse at 40% 30%, var(--pattern-a), var(--pattern-b) 75%);
  }
  .card-front__name {
    position: absolute;
    left: 230px;
    top: 168px;
    font-family: "Archivo", sans-serif;
    font-weight: 700;
    font-size: 36px;
    color: var(--white);
    letter-spacing: -0.5px;
  }
  /* Back */
  .brand {
    position: absolute;
    left: 44px;
    top: 0;
    width: 300px;
    height: 100%;
    display: flex;
    flex-direction: column;
    align-items: center;
    justify-content: center;
    gap: 18px;
  }
  .brand__dot {
    width: 64px;
    height: 64px;
    border-radius: 50%;
    background: var(--blue);
  }
  .brand__name {
    font-family: "Archivo", sans-serif;
    font-weight: 700;
    font-size: 30px;
    color: var(--white);
    letter-spacing: -0.5px;
    white-space: nowrap;
  }
  .divider {
    position: absolute;
    left: 366px;
    top: 92px;
    width: 2px;
    height: 204px;
    background: var(--blue);
  }
  .contact {
    position: absolute;
    left: 392px;
    top: 92px;
    color: var(--white);
  }
  .contact__name {
    font-size: 26px;
    font-weight: 500;
    letter-spacing: 3px;
    color: var(--blue);
    text-transform: uppercase;
    line-height: 1;
  }
  .contact__role {
    font-size: 17px;
    margin-top: 6px;
    letter-spacing: 0.5px;
  }
  .contact__address {
    font-size: 17px;
    font-style: normal;
    line-height: 1.35;
    margin-top: 18px;
    letter-spacing: 0.5px;
  }
  .contact__list { list-style: none; margin-top: 4px; }
  .contact__item {
    display: flex;
    align-items: center;
    gap: 8px;
    font-size: 17px;
    line-height: 1.4;
    letter-spacing: 0.5px;
  }
  .contact__icon { width: 13px; height: 13px; flex: none; }
</style>
</head>
<body>
  <section class="card card-front">
    <div class="card-front__pattern" role="img" aria-label="Repeating pattern of the company mark in subtle raised gloss on black"></div>
    <p class="card-front__name">Ridgeline Electrical</p>
  </section>

  <section class="card card-back">
    <div class="brand">
      <span class="brand__dot"></span>
      <p class="brand__name">Ridgeline Electrical</p>
    </div>
    <div class="divider"></div>
    <div class="contact">
      <h1 class="contact__name">Daniel Hartley</h1>
      <p class="contact__role">Founder</p>
      <address class="contact__address">418 Alder Crest Road<br>Kettle Falls, WA 99141</address>
      <ul class="contact__list">
        <li class="contact__item">
          <svg class="contact__icon" viewBox="0 0 24 24" fill="var(--blue)"><path d="M6.6 10.8a15.1 15.1 0 0 0 6.6 6.6l2.2-2.2c.3-.3.7-.4 1-.2 1.1.4 2.3.6 3.6.6.6 0 1 .4 1 1V20c0 .6-.4 1-1 1C10.6 21 3 13.4 3 4c0-.6.4-1 1-1h3.5c.6 0 1 .4 1 1 0 1.3.2 2.5.6 3.6.1.3 0 .7-.2 1z"/></svg>
          <span>555 014 2283</span>
        </li>
        <li class="contact__item">
          <svg class="contact__icon" viewBox="0 0 24 24" fill="none" stroke="var(--blue)" stroke-width="2"><rect x="3" y="5" width="18" height="14" rx="1"/><path d="M3 6l9 7 9-7"/></svg>
          <span>hello@ridgelineelectric.com</span>
        </li>
        <li class="contact__item">
          <svg class="contact__icon" viewBox="0 0 24 24" fill="none" stroke="var(--blue)" stroke-width="2"><circle cx="12" cy="12" r="9"/><path d="M3 12h18M12 3c3 3 3 15 0 18M12 3c-3 3-3 15 0 18"/></svg>
          <span>ridgelineelectric.com</span>
        </li>
      </ul>
    </div>
  </section>
</body>
</html>
```